Carpentry company Needs a business card design

We need a design for a Carpentry / building company, business card. Please think of designs out of the ordinary and try to make it eye catching. Our existing logo will need to be incorporated in the design. However feel free to change the colours of the logo to suit your design. I would like to see some designs with green /black and orange incorporated into it.These are not the only colours accepted and all designs that appeal will be accepted.

Please contact me should you have any questions
Thanks Martin

Target Market(s)

General Public seeking carpentry work

Industry/Entity Type

Business

Contact Information for Business Card

- Current company logo ( colours can be changed)
-Phone number ,
- info@brelvanbuild.com.au
- brelvanbuild.com.au
-the facebook symbol

Font styles to use
Other font styles liked:
• You choose

Requirements
Must have
• Services we provide
• - Renovations
• -Deckings & Pergolas
• -Kitchens
• - Bathrooms
• - Intricate details
Nice to have
• an awesome design
Should not have
• Tools on the business card

```html
<!DOCTYPE html>
<html lang="en">
<head>
<meta charset="utf-8">
<title>Brelvan Build – Business Card</title>
<link rel="stylesheet" href="https://fonts.googleapis.com/css2?family=Oswald:wght@400;500;700&family=Michroma&display=swap">
<style>
  :root {
    --backdrop: #e8eaed;
    --card: #fdfbe6;
    --ink: #0c0c0c;
    --orange: #e8603c;
    --teal: #1f9e9a;
  }
  * { box-sizing: border-box; margin: 0; padding: 0; }
  html, body {
    width: 1200px; height: 900px; overflow: hidden;
    background: var(--backdrop);
  }
  .card {
    position: absolute; top: 322px;
    width: 450px; height: 258px;
    background: var(--card);
    overflow: hidden;
  }
  .card--front { left: 132px; }
  .card--back { left: 602px; }
  .card__art { position: absolute; inset: 0; }

  .brand {
    position: absolute; display: flex; align-items: center; gap: 6px;
    font-family: "Oswald", sans-serif; font-weight: 700;
    color: var(--ink); letter-spacing: 0.4px; line-height: 1;
    white-space: nowrap;
  }
  .brand__mark { width: 9px; height: 9px; background: var(--teal); flex: none; }
  .brand--front { left: 26px; top: 48px; font-size: 21px; }
  .brand--back { left: 296px; top: 204px; font-size: 18px; }
  .brand--back .brand__mark { background: var(--orange); }

  .rule-under-brand {
    position: absolute; left: 25px; top: 107px; width: 160px;
    border-top: 1.5px dashed var(--teal);
  }
  .divider {
    position: absolute; left: 194px; top: 40px; width: 0; height: 128px;
    border-left: 1.5px solid var(--teal);
  }
  .contact {
    position: absolute; left: 27px; top: 116px;
    list-style: none; white-space: nowrap;
    font-family: "Oswald", sans-serif; font-weight: 400; font-size: 11px;
    letter-spacing: 0.3px; color: var(--teal); line-height: 19px;
  }
  .contact__label { color: var(--orange); font-weight: 700; margin-right: 8px; }

  .services { position: absolute; left: 208px; top: 40px; }
  .services__title {
    font-family: "Oswald", sans-serif; font-weight: 500;
    font-size: 26px; color: var(--ink); line-height: 1; letter-spacing: 0.3px;
  }
  .services__list {
    list-style: none; margin-top: 9px;
    font-family: "Michroma", sans-serif; font-size: 8.2px;
    letter-spacing: 1.6px; color: var(--orange); line-height: 20px;
  }

  .web {
    position: absolute; left: 28px; top: 200px;
    display: flex; align-items: center; gap: 14px;
    font-family: "Michroma", sans-serif; font-size: 11px;
    letter-spacing: 2.4px; color: var(--orange); white-space: nowrap;
  }
  .web__icon { width: 11px; height: 11px; background: var(--orange); }
</style>
</head>
<body>

<section class="card card--front" aria-label="Business card front">
  <svg class="card__art" viewBox="0 0 450 258" aria-hidden="true">
    <polygon points="0,190 305,190 360,140 410,190 450,190 450,258 0,258" fill="var(--ink)"/>
    <polyline points="0,178 305,178 360,127 420,178 450,178" fill="none"
      stroke="var(--teal)" stroke-width="1.2" stroke-dasharray="4 3"/>
  </svg>

  <div class="brand brand--front"><span class="brand__mark"></span>BRELVAN BUILD</div>
  <div class="rule-under-brand"></div>
  <div class="divider"></div>

  <ul class="contact">
    <li><span class="contact__label">M.</span>0412.555.018</li>
    <li><span class="contact__label">E.</span>INFO@BRELVANBUILD.COM.AU</li>
  </ul>

  <div class="services">
    <h2 class="services__title">SERVICES WE OFFER</h2>
    <ul class="services__list">
      <li>DECKINGS &amp; PERGOLAS</li>
      <li>INTRICATE DETAILS</li>
      <li>RENOVATIONS</li>
      <li>BATHROOMS</li>
      <li>KITCHENS</li>
    </ul>
  </div>

  <div class="web"><span class="web__icon"></span>WWW.BRELVANBUILD.COM.AU</div>
</section>

<section class="card card--back" aria-label="Business card back">
  <svg class="card__art" viewBox="0 0 450 258" aria-hidden="true">
    <polygon points="0,0 103,0 103,32 48,88 103,142 103,258 0,258" fill="var(--ink)"/>
    <polyline points="109,0 109,34 56,88 109,140 109,258" fill="none"
      stroke="var(--orange)" stroke-width="1.2" stroke-dasharray="4 3"/>
    <polyline points="116,0 116,37 65,88 116,137 116,258" fill="none"
      stroke="var(--orange)" stroke-width="1.2" stroke-dasharray="4 3"/>
  </svg>

  <div class="brand brand--back"><span class="brand__mark"></span>BRELVAN BUILD</div>
</section>

</body>
</html>
```